Pure Palm tree rhum label design

We need a label design for a palm tree rhum named 'Voile Doré'. We have an original design and we need an enhancement or a new design that reflects the product. It is a liquor. The label should be bilingual (French and English). We have original design that gives an idea and can be used as starting point. The text on the label for the existing design has to show up in the new design. The text is uploaded too as well as the existing design.
Update:
- The design must use Oil Palm Tree and not Palm Tree. Sample Images are attached.
- The neck of the bottle has to have the name of the product: Voile Doré.
- The word 'Liqueur' goes between the volume (1L) and the percentage of alcohol (43% Vol).
- Back side text is provided: see document
- The following description goes between the English and the french version (front and back):
The word: L'Original
The representation of a palm oil tree
The word: Original.
An image is uploaded for that.
No mandatory Fonts or Color or Bakground.

Font styles to use
Serif
Sans Serif
Script

```html
<!DOCTYPE html>
<html lang="fr">
<head>
<meta charset="utf-8">
<title>Voile Corail – Saveur Tropicale</title>
<link href="https://fonts.googleapis.com/css2?family=Marcellus&family=Dancing+Script:wght@700&family=PT+Serif&family=Poppins:wght@300&display=swap" rel="stylesheet">
<style>
  :root {
    --page: #ffffff;
    --label: #000000;
    --rule: #6b6d70;
    --emblem: #5a5c5f;
    --ink: #ffffff;
  }
  html, body {
    margin: 0;
    padding: 0;
    width: 1016px;
    height: 1200px;
    overflow: hidden;
    background: var(--page);
  }
  .canvas {
    position: relative;
    width: 1016px;
    height: 1200px;
  }
  .label-shape {
    position: absolute;
    inset: 0;
  }
  .emblem {
    position: absolute;
    left: 434px;
    top: 188px;
    width: 148px;
    height: 156px;
    background: radial-gradient(ellipse at 50% 35%, var(--emblem), #2a2b2d 75%, transparent 76%);
  }
  .tagline {
    position: absolute;
    top: 298px;
    width: 100px;
    text-align: center;
    font-family: "Poppins", sans-serif;
    font-weight: 300;
    font-size: 18px;
    color: var(--ink);
    padding-bottom: 6px;
    border-bottom: 2px solid var(--rule);
  }
  .tagline--fr { left: 374px; }
  .tagline--en { left: 542px; }
  .product-name {
    position: absolute;
    top: 342px;
    left: 0;
    width: 1016px;
    margin: 0;
    text-align: center;
    font-family: "Marcellus", serif;
    font-weight: 400;
    font-size: 62px;
    line-height: 1;
    color: var(--ink);
  }
  .flavour {
    position: absolute;
    top: 420px;
    left: 0;
    width: 1016px;
    text-align: center;
    font-family: "Dancing Script", cursive;
    font-weight: 700;
    font-size: 32px;
    color: var(--ink);
  }
  .description {
    position: absolute;
    left: 168px;
    width: 680px;
    margin: 0;
    text-align: center;
    font-family: "PT Serif", serif;
    font-size: 20px;
    line-height: 31.3px;
    color: var(--ink);
  }
  .description--fr { top: 481px; }
  .description--en { top: 723px; }
  .wave-band {
    position: absolute;
    left: 138px;
    top: 953px;
    width: 741px;
    height: 106px;
    background: linear-gradient(180deg, #1a1a1a, #3c3d3f);
  }
</style>
</head>
<body>
<main class="canvas">
  <svg class="label-shape" width="1016" height="1200" viewBox="0 0 1016 1200" aria-hidden="true">
    <path d="M94,1107 V560 A415,413 0 0 1 924,560 V1107 Z" fill="var(--label)"/>
    <path d="M138,1063 V560 A370,376 0 0 1 879,560 V1063 Z" fill="none" stroke="var(--rule)" stroke-width="2.5"/>
  </svg>

  <div class="emblem" role="img" aria-label="Illustration d'un palmier à huile"></div>
  <span class="tagline tagline--fr">L'Original</span>
  <span class="tagline tagline--en">Original</span>

  <h1 class="product-name">Voile Corail</h1>
  <div class="flavour">Saveur Tropicale</div>

  <p class="description description--fr">
    Le Sodabi constitue un reflet d'une culture, un<br>
    patrimoine. Le produit garde ses valeurs d’origine, de<br>
    convivialité et d’authenticité. Le Voile Corail répond à un<br>
    besoin d’élaboration de nouveaux produits à base du<br>
    Sodabi artisanal et des fruits tropicaux, allie avec<br>
    savoir-faire, tradition et tendance pour offrir aux adeptes<br>
    de ce spiritueux de meilleurs moments de convivialité.
  </p>

  <p class="description description--en" lang="en">
    Sodabi is a reflection of a culture, a heritage.<br>
    The product retains its original values, friendliness<br>
    and authenticity. The Voile Corail responds to a need<br>
    for the development of new products based on artisanal<br>
    Sodabi and tropical fruits, combines know-how,<br>
    tradition and trend to offer fans of this spirit<br>
    better moments of conviviality.
  </p>

  <div class="wave-band" role="img" aria-label="Motif décoratif de vagues"></div>
</main>
</body>
</html>
```